This design will be for the label and logo of Dame Rosa Tequila. The design needs to be on a bottle, using the primary color turquoise, white and navy blue. You can also use Burnt Orange or Light blue or another color that you think goes well with Turquoise. Dame Rosa is a tequila that is inspired by a beachy, campy, coastal, ocean, nautical feel. It's a modern feeling brand. The text should simply say "Dame Rosa Tequila" and also a logo or mark in or around the text. Please place the logo and lettering on a bottle (I have attached an example ) and put the other necessary details such as: 100% Agave, 750ml , 40% alc, 80 proof, Blanco Tequila. Dame Rosa was a pirate, but we want her inspiration to be modern and not literal. I've attached some inspiration for the clean look we're going for.

Dame Rosa Tequila

```html
<!DOCTYPE html>
<html lang="en">
<head>
<meta charset="utf-8">
<title>Dame Rosa Tequila – Blanco Label</title>
<link rel="stylesheet" href="https://fonts.googleapis.com/css2?family=Cinzel:wght@400&family=Cormorant+Garamond:wght@600&family=Montserrat:wght@500;800&display=swap">
<style>
  :root {
    --turquoise: #00ffe8;
    --navy: #06062b;
    --burnt-orange: #f0913a;
    --paper: #ffffff;
  }
  html, body {
    margin: 0;
    padding: 0;
    width: 1200px;
    height: 869px;
    overflow: hidden;
    background: var(--paper);
  }
  .label {
    position: relative;
    width: 1200px;
    height: 869px;
    background: var(--paper);
    color: var(--navy);
  }
  .brand-mark {
    position: absolute;
    left: 540px;
    top: 108px;
    width: 120px;
    height: 120px;
    border-radius: 50%;
    background: var(--turquoise);
  }
  .brand-name {
    position: absolute;
    left: 0;
    width: 1200px;
    top: 300px;
    margin: 0;
    text-align: center;
    font-family: "Cinzel", serif;
    font-weight: 400;
    font-size: 118px;
    line-height: 1;
    letter-spacing: 2px;
    color: var(--turquoise);
  }
  .category {
    position: absolute;
    left: 275px;
    width: 642px;
    top: 432px;
    display: flex;
    align-items: center;
    gap: 16px;
  }
  .category-rule {
    flex: 1;
    height: 3px;
    background: var(--navy);
  }
  .category-text {
    font-family: "Cinzel", serif;
    font-size: 46px;
    line-height: 1;
    letter-spacing: 2px;
    color: var(--turquoise);
  }
  .specs {
    position: absolute;
    left: 242px;
    top: 509px;
    width: 716px;
    height: 138px;
    border-top: 3px solid var(--burnt-orange);
    display: flex;
  }
  .spec {
    flex: 1;
    text-align: center;
    font-family: "Cormorant Garamond", serif;
    font-weight: 600;
    color: var(--navy);
    padding-top: 14px;
  }
  .spec + .spec { border-left: 3px solid var(--burnt-orange); }
  .spec-value { display: block; font-size: 50px; line-height: 1.1; letter-spacing: 3px; }
  .spec-unit { display: block; font-size: 64px; line-height: 1.05; letter-spacing: 1px; }
  .volume {
    position: absolute;
    left: 244px;
    top: 762px;
    font-family: "Montserrat", sans-serif;
    font-weight: 500;
    font-size: 66px;
    line-height: 1;
    color: var(--navy);
  }
  .expression {
    position: absolute;
    left: 616px;
    top: 689px;
    width: 356px;
    height: 130px;
  }
  .expression svg { position: absolute; inset: 0; }
  .expression-text {
    position: absolute;
    inset: 0;
    display: flex;
    align-items: center;
    justify-content: center;
    font-family: "Montserrat", sans-serif;
    font-weight: 800;
    font-size: 76px;
    color: var(--paper);
    letter-spacing: 1px;
  }
</style>
</head>
<body>
<main class="label">
  <div class="brand-mark" aria-hidden="true"></div>
  <h1 class="brand-name">Dame Rosa</h1>
  <div class="category">
    <span class="category-rule"></span>
    <span class="category-text">TEQUILA</span>
    <span class="category-rule"></span>
  </div>
  <section class="specs">
    <div class="spec"><span class="spec-value">100%</span><span class="spec-unit">AGAVE</span></div>
    <div class="spec"><span class="spec-value">40%</span><span class="spec-unit">ALC</span></div>
    <div class="spec"><span class="spec-value">40</span><span class="spec-unit">PROOF</span></div>
  </section>
  <div class="volume">750ml</div>
  <div class="expression">
    <svg viewBox="0 0 356 130" width="356" height="130" aria-hidden="true">
      <path fill="var(--navy)" d="M32 0 H324 V20 A45 45 0 0 1 356 62 V68 A45 45 0 0 1 324 110 V130 H32 V110 A45 45 0 0 1 0 68 V62 A45 45 0 0 1 32 20 Z"/>
    </svg>
    <span class="expression-text">BLANCO</span>
  </div>
</main>
</body>
</html>
```